HARLOWE CONSERVATORY SAXOPHONE SENIOR RECITAL

I need a poster design for my senior saxophone recital. The title of it is "Quill: a Voyage beneath the Edge of Tone". My concept is completely contrasting to the idea of a typical university recital. I'm so put off by the idea of "clap..clap..{play some music}..clap..clap..repeat". My recital is all based off of sound. The music I selected is all very modern (i.e Brem Ostrakel 'Warm from the First Pour' for Saxophone and Coffee Machine). I've included the Chatterbox link so you can see the picture I have in the background. I like the idea of minimal black and white photography. Also, I would like the time / date / location / etc. all included on it. Let your imaginations run wild! It's art for an artist!
https://www.chatterbox-example.net/events/412093857716230/
Target Market(s)
University Students around the Harlowe Conservatory and locals around the art district of South Beach, FL.
Industry/Entity Type
University
Look and feel

```html
<!DOCTYPE html>
<html lang="en">
<head>
<meta charset="utf-8">
<title>Quill: a Voyage beneath the Edge of Tone</title>
<link rel="stylesheet" href="https://fonts.googleapis.com/css2?family=Josefin+Sans:wght@300;400;600;700&display=swap">
<style>
  :root {
    --stage: #0e0e0e;
    --sky-top: #c9c9c9;
    --sky-mid: #b4b4b4;
    --cloud-dark: #9e9e9e;
    --horizon: #a8a8a8;
    --horizon-glow: #d8d8d8;
    --water: #9a9a9a;
    --water-deep: #8a8a8a;
    --ink: #2a2a2a;
    --panel: rgba(214, 214, 214, 0.78);
    --light-text: #f2f2f2;
  }
  * { margin: 0; padding: 0; box-sizing: border-box; }
  html, body {
    width: 1200px;
    height: 786px;
    overflow: hidden;
    background: var(--stage);
    font-family: "Josefin Sans", sans-serif;
  }
  .poster {
    position: absolute;
    left: 322px;
    top: 0;
    width: 556px;
    height: 786px;
    overflow: hidden;
  }
  .poster__photo {
    position: absolute;
    inset: 0;
    background:
      /* faint shoreline glow on the horizon */
      linear-gradient(90deg, transparent 0%, transparent 52%, rgba(230,230,230,0.55) 60%, rgba(230,230,230,0.55) 98%, transparent 100%)
        0 514px / 100% 4px no-repeat,
      /* bright mist in upper sky */
      radial-gradient(ellipse 70% 22% at 35% 8%, rgba(225,225,225,0.6), transparent 75%),
      /* dark cloud bank above the horizon */
      radial-gradient(ellipse 80% 14% at 70% 58%, rgba(140,140,140,0.55), transparent 75%),
      radial-gradient(ellipse 60% 12% at 25% 52%, rgba(150,150,150,0.45), transparent 75%),
      /* soft reflection on the water */
      radial-gradient(ellipse 45% 20% at 55% 78%, rgba(185,185,185,0.45), transparent 75%),
      linear-gradient(180deg,
        var(--sky-top) 0%,
        var(--sky-mid) 35%,
        var(--cloud-dark) 55%,
        var(--horizon) 64.5%,
        var(--horizon-glow) 65.6%,
        var(--water) 67%,
        var(--water-deep) 100%);
  }
  .title {
    position: absolute;
    left: 130px;
    top: 0;
    width: 306px;
    color: var(--ink);
  }
  .title__main {
    position: absolute;
    top: 100px;
    left: 0;
    width: 316px;
    font-size: 82px;
    font-weight: 700;
    letter-spacing: 10px;
    line-height: 1;
    text-align: left;
    white-space: nowrap;
  }
  .title__panel {
    position: absolute;
    top: 178px;
    left: 0;
    width: 306px;
    height: 128px;
    background: var(--panel);
  }
  .title__sub {
    position: absolute;
    top: 187px;
    right: 6px;
    list-style: none;
    text-align: right;
    font-size: 21px;
    font-weight: 300;
    letter-spacing: 1.5px;
    line-height: 28px;
  }
  .title__tail {
    position: absolute;
    top: 310px;
    right: -6px;
    font-size: 30px;
    font-weight: 600;
    letter-spacing: 6px;
    white-space: nowrap;
  }
  .details {
    position: absolute;
    left: 202px;
    top: 684px;
    width: 150px;
    color: var(--light-text);
    text-align: center;
    font-size: 25px;
    font-weight: 400;
    letter-spacing: 1.5px;
  }
  .details__location {
    padding-bottom: 8px;
    border-bottom: 1.5px solid var(--light-text);
  }
  .details__when { padding-top: 10px; }
</style>
</head>
<body>
  <main class="poster">
    <div class="poster__photo" role="img" aria-label="Misty black and white photograph of a woman in a pale dress standing in still water, looking out toward a foggy horizon"></div>

    <h1 class="title">
      <span class="title__main">QUILL</span>
      <span class="title__panel"></span>
      <ul class="title__sub">
        <li>A</li>
        <li>VOYAGE</li>
        <li>BENEATH</li>
        <li>THE</li>
      </ul>
      <span class="title__tail">EDGE OF TONE</span>
    </h1>

    <div class="details">
      <p class="details__location">LOCATION</p>
      <p class="details__when">DATE TIME</p>
    </div>
  </main>
</body>
</html>
```